Presentation pour application de menu digitale

Je souhaite créer un flyer de présentation pour une application de menu digitale afin de la présenter à mes futurs clients. Cette application aura aussi vocation de premier réseau social culinaire pour les utilisateurs finaux.
Merci de récupérer le texte du site platboreal.tech
Le flyer sera imprimé au format A3 pliable pour en faire un format A4.
Le logo et les images que vous récupérerez seront en vernis sélectif.

Target Market(s)

restaurateur

Industry/Entity Type

Restaurateur

Font styles to use
Sans Serif

Colors
59FF00
82FF00
B8FF75
E3FFCB
F4FFEA
6B429C
8869AF
B7A5CE
E3DAEB
F3F0F8

```html
<!DOCTYPE html>
<html lang="fr">
<head>
<meta charset="utf-8">
<title>Platboréal – dépliant</title>
<link rel="stylesheet" href="https://fonts.googleapis.com/css2?family=Montserrat:ital,wght@0,400;0,500;0,600;0,700;0,800;1,600&display=swap">
<style>
  :root{
    --purple:#6b429c;
    --purple-mid:#8869af;
    --purple-soft:#b7a5ce;
    --purple-pale:#e3daeb;
    --green:#8cc63f;
    --green-card:#bcd96b;
    --ink:#113c3a;
    --paper:#ffffff;
    --grey:#f0f0f0;
    --stage:#f2f2f2;
  }
  *{margin:0;padding:0;box-sizing:border-box}
  html,body{width:1200px;height:848px;overflow:hidden}
  body{background:var(--stage);font-family:'Montserrat',sans-serif;color:var(--ink);position:relative}
  .spread{position:absolute;top:219px;width:580px;height:409px;overflow:hidden;background:var(--paper)}
  .spread--outer{left:13px}
  .spread--inner{left:607px;background:var(--grey)}
  .abs{position:absolute}

  /* outer spread */
  .pro-panel{left:0;top:0;width:184px;height:232px;background:var(--paper);padding:14px 10px 0 32px}
  .pro-panel h3{font-size:5.6px;font-weight:500;margin-bottom:9px}
  .pro-panel ul{list-style:disc;padding-left:9px}
  .pro-panel li{font-size:5.6px;line-height:9.1px;margin-bottom:0}
  .venue-photo{left:184px;top:0;width:106px;height:202px;background:linear-gradient(160deg,#6d5330 0%,#2b2014 45%,#b18c48 80%,#3a2c1b 100%)}
  .join{left:42px;top:205px;font-size:11.5px;font-weight:700;line-height:12px;color:var(--ink)}
  .band-purple{left:0;width:580px;background:var(--purple)}
  .hero{left:290px;top:0;width:290px;height:221px}
  .hero-title{left:8px;top:103px;color:#fff;font-size:12px;font-weight:800;line-height:10px}
  .brand{display:flex;align-items:center;gap:3px;font-weight:700;color:var(--ink)}
  .brand i{display:block;border-radius:50%;background:var(--green)}
  .hero .brand{position:absolute;left:118px;top:32px;font-size:8px}
  .hero .brand i{width:7px;height:7px}
  .devices{left:150px;top:82px;width:122px;height:126px;border-radius:8px;background:linear-gradient(135deg,#c9b79e,#f4f1ee 60%,#dcd8d0)}
  .plans{left:0;top:245px;display:flex}
  .plan{position:absolute;top:0;width:55px;height:67px;background:var(--green-card);border-radius:2px;text-align:center;color:var(--purple);padding-top:12px}
  .plan h4{font-size:4.6px;font-weight:500;color:#4a5a2a}
  .plan strong{display:block;font-size:16px;font-weight:700;line-height:17px;color:var(--purple-mid)}
  .plan strong small{font-size:3px;font-weight:500}
  .plan p{font-size:2.7px;line-height:3.6px;color:#6b7f3a;padding:2px 6px 0}
  .who{left:296px;top:244px;color:#fff;font-size:15.5px;font-weight:800;line-height:14px}
  .who-text{left:389px;top:242px;width:200px;color:#fff;font-size:4.8px;line-height:5.7px;padding-right:20px}
  .rule{height:1.5px;background:var(--purple)}
  .what{right:23px;top:310px;text-align:right}
  .what h4{font-size:9px;font-weight:800;line-height:8.5px}
  .what p{font-size:4.4px;line-height:5.2px;margin-top:7px;width:64px;margin-left:auto}
  .web-band{left:0;top:333px;width:580px;height:31px}
  .web{left:32px;top:343px;color:#fff;font-size:5.6px;font-weight:600;font-style:italic}
  .footer{left:0;top:364px;width:580px;height:45px;background:var(--purple)}
  .contact{left:0;top:384px;width:580px;text-align:center;padding-right:70px;color:#fff;font-size:5.6px;font-style:italic}

  /* inner spread */
  .food-band{left:0;top:0;width:580px;height:128px;background:linear-gradient(120deg,#93b24a 0%,#7fa03a 50%,#a2b75a 100%)}
  .food-band-edge{left:0;top:128px;width:580px;height:4px;background:var(--purple-mid)}
  .intro{left:43px;top:16px;width:232px;color:#fff}
  .intro .brand{justify-content:center;font-size:10px;margin:0 0 24px 60px;color:var(--ink)}
  .intro .brand i{width:9px;height:9px}
  .intro p{font-size:5.4px;line-height:7.3px}
  .lower-white{left:0;top:243px;width:433px;height:138px;background:var(--paper)}
  .mission{left:43px;top:140px;width:225px}
  .mission h2{font-size:13px;font-weight:700;margin-bottom:7px}
  .mission p{font-size:5.4px;line-height:8.3px}
  .how{left:43px;top:206px;font-size:13px;font-weight:700}
  .step{position:absolute;width:111px;background:var(--purple);border-radius:2px;padding:0 8px;color:#fff}
  .step .icon{width:24px;height:28px;margin:14px 0 0 0;border-radius:3px;background:linear-gradient(160deg,#f4c8a8,#e59a76)}
  .step h3{font-size:9.5px;font-weight:700;line-height:11px;color:var(--purple-soft);margin-top:22px}
  .step p{font-size:5.8px;line-height:8.4px;margin-top:7px}
  .features{left:443px;top:172px;width:124px}
  .features h2{font-size:13px;font-weight:700;margin-bottom:14px}
  .features h4{font-size:5.4px;font-weight:500;margin-bottom:10px}
  .features p{font-size:5.4px;line-height:9.1px}
  .bottom-band{left:0;top:381px;width:580px;height:28px}
</style>
</head>
<body>

<!-- Volet extérieur -->
<section class="spread spread--outer">
  <div class="abs band-purple" style="top:202px;height:75px"></div>
  <div class="abs band-purple" style="left:290px;top:210px;width:290px;height:30px"></div>

  <div class="abs pro-panel">
    <h3>Pour les restaurateurs</h3>
    <ul>
      <li>Engagement client amélioré : Fidélisez votre clientèle grâce à une expérience interactive et personnalisée.</li>
      <li>Analyse des préférences : Obtenez des données précieuses sur les choix et préférences de vos clients pour mieux adapter vos offres.</li>
      <li>Mettez en avant les plats que vous souhaitez vendre : Grace à l’option Push mettez en avant les plats que vous souhaitez vendre en priorité.</li>
      <li>Gains de temps : Grace à la préparation de commande vos serveurs passent moins de temps à prendre la commande à chaque table.</li>
      <li>Promotion virale : Profitez du partage social entre utilisateurs pour augmenter la visibilité de votre établissement.</li>
    </ul>
  </div>
  <div class="abs join">Rejoignez la<br>communauté Platboréal</div>

  <div class="abs venue-photo" role="img" aria-label="Photo d’une salle de restaurant chaleureuse aux tons dorés"></div>

  <div class="abs hero">
    <svg class="abs" style="left:0;top:0" width="290" height="221" viewBox="0 0 290 221">
      <rect width="290" height="221" fill="#e7e3dd"/>
      <polygon points="199,0 290,0 290,77 226,77" fill="#6b429c"/>
      <polygon points="0,20 52,20 126,221 0,221" fill="#8869af"/>
      <polygon points="43,20 54,20 124,221 112,221" fill="#8cc63f"/>
      <polygon points="0,68 111,68 140,164 0,164" fill="#6b429c"/>
      <polygon points="0,164 90,164 108,221 0,221" fill="#8869af"/>
      <line x1="145" y1="222" x2="290" y2="220" stroke="#ffffff" stroke-width="0.6"/>
    </svg>
    <div class="brand"><i></i>Platboréal</div>
    <div class="abs devices" role="img" aria-label="Deux smartphones affichant l’application de menu digital"></div>
    <div class="abs hero-title">Le 1er réseau<br>social culinaire</div>
  </div>

  <div class="abs who">Qui nous<br>sommes?</div>
  <p class="abs who-text">Plongez au cœur d’une révolution culinaire avec notre application de menu digital, conçue pour enrichir votre expérience au restaurant. Platboréal va au-delà d’un simple menu : c’est une plateforme où vous pouvez préparer vos commandes, sauvegarder vos plats favoris, et partager vos expériences avec vos amis. En d’autre termes, le premier réseau social pour restaurants.</p>

  <div class="abs plans">
    <div class="plan" style="left:50px"><h4>Silver</h4><strong>99<small>/mois</small></strong><p>Menu digital complet, QR codes inclus, support par email</p></div>
    <div class="plan" style="left:117px"><h4>Gold</h4><strong>129<small>/mois</small></strong><p>Option Push, statistiques clients, commandes à table, support prioritaire</p></div>
    <div class="plan" style="left:184px"><h4>Platinum</h4><strong>179<small>/mois</small></strong><p>Toutes les options, multi-sites, accompagnement dédié</p></div>
  </div>

  <div class="abs rule" style="left:293px;top:295px;width:158px"></div>
  <div class="abs what">
    <h4>Ce que nous<br>faisons</h4>
    <p>Dive into the heart of a culinary revolution with our digital menu application, designed to enrich your restaurant experience.</p>
  </div>

  <svg class="abs web-band" width="580" height="31" viewBox="0 0 580 31">
    <polygon points="0,0 472,0 488,31 0,31" fill="#8869af"/>
    <polygon points="472,0 480,0 489,31 481,31" fill="#8cc63f"/>
  </svg>
  <div class="abs web">www.platboreal.tech</div>
  <div class="abs" style="left:115px;top:346px;width:158px;height:0.8px;background:#fff"></div>
  <div class="abs footer"></div>
  <div class="abs contact">555-010-2030 | hello@platboreal.tech</div>
</section>

<!-- Volet intérieur -->
<section class="spread spread--inner">
  <div class="abs food-band" role="img" aria-label="Photo d’un plat de salade verte en teinte verte"></div>
  <div class="abs food-band-edge"></div>
  <div class="abs intro">
    <div class="brand"><i></i>Platboréal</div>
    <p>Plongez au cœur d’une révolution culinaire avec notre application de menu digital, conçue pour enrichir votre expérience au restaurant. Platboréal va au-delà d’un simple menu : c’est une plateforme où vous pouvez préparer vos commandes, sauvegarder vos plats favoris, et partager vos expériences avec vos amis. En d’autre termes, le premier réseau social pour restaurants</p>
  </div>

  <div class="abs lower-white"></div>
  <div class="abs mission">
    <h2>Notre mission</h2>
    <p>Rendre chaque sortie au restaurant aussi fluide et agréable que possible. Avec Platboréal, chaque visite est personnalisée et connectée. Dès votre arrivée, scannez un QR code ou RFC pour accéder au menu et commencez votre expérience culinaire unique.</p>
  </div>
  <h2 class="abs how">Comment ça marche?</h2>

  <article class="step" style="left:43px;top:237px;height:131px">
    <div class="icon" role="img" aria-label="Main tenant un téléphone qui scanne un QR code"></div>
    <h3>1. Scannez le QR code</h3>
    <p>À votre arrivée, scannez le code pour débloquer le menu interactif de votre restaurant.</p>
  </article>
  <article class="step" style="left:169px;top:237px;height:131px">
    <div class="icon" role="img" aria-label="Main tenant un téléphone affichant le menu"></div>
    <h3>2. Découvrez</h3>
    <p>À votre arrivée, scannez le code pour débloquer le menu interactif de votre restaurant.</p>
  </article>
  <article class="step" style="left:312px;top:29px;height:132px">
    <div class="icon" role="img" aria-label="Main tenant un téléphone pour choisir des plats"></div>
    <h3>3. Choisissez</h3>
    <p>Préparez votre commande</p>
  </article>
  <article class="step" style="left:442px;top:29px;height:132px">
    <div class="icon" role="img" aria-label="Main tenant un téléphone avec une liste de favoris"></div>
    <h3>4. Personnaliser et sauvegardez</h3>
    <p style="line-height:7.6px">Sélectionnez et personnalisez vos plats, sauvegardez vos favoris pour la prochaine fois, et partagez vos choix avec vos amis.</p>
  </article>
  <article class="step" style="left:312px;top:174px;height:132px">
    <div class="icon" role="img" aria-label="Main tenant un téléphone pour partager un avis"></div>
    <h3 style="margin-top:18px">5. Partagez votre expérience</h3>
    <p style="line-height:7.6px">Devenez une partie de notre réseau social de gourmets, recommandez des plats et découvrez les favoris d’autres utilisateurs.</p>
  </article>

  <div class="abs features">
    <h2>Fonctionnalités</h2>
    <h4>Pour les clients</h4>
    <p>Accès instantané via QR code : Accédez facilement au menu en scannant un QR code dès votre arrivée. Sauvegardez vos plats préférés : Créez une liste de vos favoris pour faciliter vos commandes futures. Réseau social intégré : Partagez vos préférences et découvrez les recommandations de vos amis et d’autres utilisateurs. Personnalisation avancée : Adaptez votre commande en fonction de vos goûts et exigences diététiques, à votre rythme.</p>
  </div>

  <svg class="abs bottom-band" width="580" height="28" viewBox="0 0 580 28">
    <rect y="4" width="580" height="24" fill="#8cc63f"/>
    <polygon points="122,0 580,0 580,28 103,28" fill="#6b429c"/>
  </svg>
</section>

</body>
</html>
```